Environmentally friendly Home and Office cleaning service needs a logo and web design!

Maple Sparkle is a new startup looking for a logo and web design. We're base in Ottawa, Canada, and all of our products are eco-friendly, as well as being easy on the sensitivities of our clients.
We wash windows, walls, kitchens, bathrooms, dust, vacuum and wash floors on our hands and knees, and bring all of our own gear and supplies.
tidyroost.example was my last website. It's functional, not bad - but just isn't great. I'm looking for a simple design, with few links or clickable buttons.
Colours I will leave to your creative mind to decide. I just want to see something that is relevant to "Maple Sparkle."

Target Market(s)

Often it's women and gay men, ages 35-70
White collar government workers, usually with pets (cats, dogs)

Industry/Entity Type

Cleaning Service

Logo Text

Maple Sparkle

Number of Pages Required

1 page

Font styles to use
Sans Serif

Colors

Designer to choose colors to be used in the design.

Requirements
Must have
• Colour, pictures

```html
<!DOCTYPE html>
<html lang="en">
<head>
<meta charset="utf-8">
<title>Maple Sparkle — Eco Cleaning</title>
<link rel="stylesheet" href="https://fonts.googleapis.com/css2?family=Open+Sans:wght@400;600;700&family=Roboto+Condensed:wght@700&display=swap">
<style>
:root{
  --green-dark:#1f6b12;
  --green-light:#a9c76a;
  --green-pale:#c8dc98;
  --ink:#222;
  --text:#555;
  --muted:#777;
  --footer:#232323;
  --white:#fff;
}
*{margin:0;padding:0;box-sizing:border-box}
html,body{width:1200px;height:2683px;overflow:hidden;background:var(--white)}
body{position:relative;font-family:"Open Sans",Arial,sans-serif;color:var(--text)}
.abs{position:absolute}

/* header */
.logo-mark{position:absolute;border-radius:50%;background:var(--green-pale);border:3px solid var(--green-light)}
.brand{position:absolute;font-weight:700;color:var(--ink);font-size:21px;white-space:nowrap}
.fees{left:524px;top:36px;font-size:15px;color:#333;white-space:nowrap}
.fees b{color:var(--green-dark);font-weight:600}
.phone{left:832px;top:33px;font-size:18px;color:#333;display:flex;align-items:center;gap:8px;white-space:nowrap}
.social{display:flex;gap:10px;position:absolute}
.social span{width:20px;height:20px;border-radius:3px;background:#222}

/* nav */
.nav{left:0;top:104px;width:1200px;height:57px;background:linear-gradient(#c3da8c,#9fbf5c);border-bottom:3px solid #8db04c}
.nav a{position:absolute;top:0;height:54px;line-height:54px;color:var(--white);text-decoration:none;font-size:16px}
.nav a.active{background:var(--green-dark);width:120px;text-align:center}

/* hero */
.hero-photo{left:0;top:161px;width:1200px;height:560px;
  background:
    radial-gradient(ellipse 130px 170px at 420px 170px,rgba(92,52,34,.85),rgba(92,52,34,0) 100%),
    radial-gradient(ellipse 120px 70px at 300px 330px,rgba(240,196,40,.9),rgba(240,196,40,0) 100%),
    radial-gradient(ellipse 110px 70px at 480px 430px,rgba(236,190,40,.85),rgba(236,190,40,0) 100%),
    radial-gradient(ellipse 160px 80px at 420px 460px,rgba(160,190,205,.8),rgba(160,190,205,0) 100%),
    radial-gradient(ellipse 200px 150px at 300px 300px,rgba(70,72,76,.55),rgba(70,72,76,0) 100%),
    radial-gradient(ellipse 600px 200px at 300px 520px,rgba(190,180,165,.8),rgba(190,180,165,0) 100%),
    linear-gradient(100deg,#d8d2c8 0%,#ebe6df 35%,#f6f5f2 65%,#eef0ee 100%)}
.hero-title{left:712px;top:358px;font-family:"Roboto Condensed",Arial,sans-serif;font-weight:700;font-size:37px;color:var(--green-dark);white-space:nowrap}
.hero-sub{left:714px;top:408px;font-size:15px;font-weight:600;color:#333;white-space:nowrap}
.hero-arrow{top:449px;width:24px;height:24px;border-radius:50%;background:#777;display:flex;align-items:center;justify-content:center}

/* welcome */
.section-title{position:absolute;left:0;width:1200px;text-align:center;font-size:31px;color:var(--ink);font-weight:400}
.intro{left:176px;top:846px;width:850px;text-align:center;font-size:13px;line-height:27px;color:var(--text)}
.service{position:absolute;top:979px;width:300px;text-align:center}
.service-icon{width:106px;height:106px;border-radius:50%;background:var(--green-light);margin:0 auto;display:flex;align-items:center;justify-content:center}
.service h3{font-weight:400;font-size:22px;color:var(--ink);margin-top:20px}
.service p{font-size:12px;line-height:24px;color:var(--muted);margin-top:6px}
.service a{font-size:12px;color:var(--green-dark);text-decoration:none;display:block;margin-top:2px}

/* green feature */
.feature-bg{left:0;top:1282px;width:1200px;height:483px;
  background:
    radial-gradient(ellipse 260px 200px at 120px 380px,rgba(10,60,8,.6),rgba(10,60,8,0)),
    radial-gradient(ellipse 260px 200px at 1080px 120px,rgba(60,140,40,.5),rgba(60,140,40,0)),
    linear-gradient(135deg,#2a7a1a,#1a6410 50%,#2d7f1c)}
.feature-card{left:148px;top:1366px;width:498px;height:333px;background:var(--white);padding:41px 36px}
.feature-card h2{font-size:25px;font-weight:400;color:var(--ink);line-height:31px}
.feature-card ul{list-style:none;margin-top:11px}
.feature-card li{font-size:13.5px;line-height:27px;color:#444}
.btn{display:inline-block;margin-top:16px;background:var(--green-light);color:var(--white);font-size:11px;padding:9px 18px;border-radius:16px;text-transform:uppercase}
.feature-photo{left:646px;top:1366px;width:400px;height:333px;
  background:
    radial-gradient(ellipse 70px 60px at 230px 90px,rgba(70,40,30,.8),rgba(70,40,30,0)),
    radial-gradient(ellipse 80px 80px at 240px 170px,rgba(190,70,60,.75),rgba(190,70,60,0)),
    radial-gradient(ellipse 90px 60px at 260px 250px,rgba(40,60,95,.75),rgba(40,60,95,0)),
    radial-gradient(ellipse 200px 50px at 200px 320px,rgba(215,205,190,.9),rgba(215,205,190,0)),
    linear-gradient(90deg,#e9dcc6 0%,#f6f1e8 35%,#d8d6d2 70%,#8f949c 100%)}

/* news */
.news{position:absolute;top:1942px;width:317px}
.news-photo{height:191px;border:4px solid #eee;box-shadow:0 0 2px #ccc;position:relative}
.date{position:absolute;left:0;top:46px;width:52px;text-align:center;color:var(--white)}
.date .d{background:var(--green-dark);padding:6px 0 4px;font-size:21px;line-height:22px}
.date .d small{display:block;font-size:10px;line-height:14px}
.date .y{background:#333;padding:10px 0;font-size:14px}
.news h3{font-weight:400;font-size:16px;color:#333;margin-top:14px}
.news p{font-size:11.5px;line-height:24px;color:var(--muted);margin-top:6px}
.news a{font-size:11.5px;color:var(--green-dark);text-decoration:none}

/* footer */
.footer{left:0;top:2387px;width:1200px;height:296px;background:var(--footer)}
.foot-head{position:absolute;top:2437px;font-size:13.5px;color:var(--white);text-transform:uppercase;white-space:nowrap}
.foot-text{position:absolute;font-size:11px;line-height:23px;color:#ddd;white-space:nowrap}
.mail-input{left:663px;top:2516px;width:143px;height:28px;background:var(--white);font-size:11px;color:#999;padding:7px 8px}
.mail-btn{left:806px;top:2516px;width:60px;height:28px;background:var(--green-light);color:var(--white);font-size:11px;text-align:center;line-height:28px}
.foot-rule{left:95px;top:2602px;width:1010px;height:1px;background:#3c3c3c}
.copyright{left:0;top:2627px;width:1200px;text-align:center;font-size:11.5px;color:#ddd}
</style>
</head>
<body>

<!-- header -->
<div class="logo-mark" style="left:89px;top:12px;width:78px;height:78px"></div>
<div class="brand" style="left:181px;top:28px">MAPLE SPARKLE</div>
<div class="abs fees"><b>Fees:</b> 37.50/hour (2.5 hour minimum)</div>
<div class="abs phone">
  <svg width="15" height="15" viewBox="0 0 24 24"><path fill="#333" d="M6.6 10.8a15 15 0 0 0 6.6 6.6l2.2-2.2c.3-.3.7-.4 1-.2 1.1.4 2.3.6 3.6.6.6 0 1 .4 1 1V20c0 .6-.4 1-1 1A17 17 0 0 1 3 4c0-.6.4-1 1-1h3.5c.6 0 1 .4 1 1 0 1.3.2 2.5.6 3.6.1.3 0 .7-.2 1z"/></svg>
  613-555-0142
</div>
<div class="social" style="left:990px;top:38px"><span></span><span></span><span></span><span></span></div>

<!-- navigation -->
<nav class="abs nav">
  <a class="active" href="#" style="left:89px">Home</a>
  <a href="#" style="left:256px">About us</a>
  <a href="#" style="left:410px">Services</a>
  <a href="#" style="left:560px">How it works</a>
  <a href="#" style="left:746px">Blog</a>
  <a href="#" style="left:864px">Support</a>
  <a href="#" style="left:1009px">Contact Us</a>
</nav>

<!-- hero -->
<div class="abs hero-photo" role="img" aria-label="Photo of a cleaner in yellow gloves wiping a kitchen countertop"></div>
<svg class="abs" style="left:0;top:630px" width="1200" height="100" viewBox="0 0 1200 100">
  <path d="M0 14 Q600 130 1200 14 L1200 100 L0 100Z" fill="#fff"/>
  <path d="M0 14 Q600 130 1200 14 Q600 112 0 14Z" fill="#1f6b12"/>
</svg>
<h1 class="abs hero-title">MAPLE SPARKLE CLEANING</h1>
<p class="abs hero-sub">Let me be part of your team to keep your space clean</p>
<div class="abs hero-arrow" style="left:1057px"><svg width="10" height="10" viewBox="0 0 10 10"><path d="M6.5 1.5 3 5l3.5 3.5" stroke="#fff" stroke-width="2" fill="none"/></svg></div>
<div class="abs hero-arrow" style="left:1086px"><svg width="10" height="10" viewBox="0 0 10 10"><path d="M3.5 1.5 7 5 3.5 8.5" stroke="#fff" stroke-width="2" fill="none"/></svg></div>

<!-- welcome -->
<h2 class="section-title" style="top:788px">Welcome To MAPLE SPARKLE</h2>
<p class="abs intro">i will give your home the respect it deserves with careful attention to detail and thorough work. it can be a relief to know that you can leave and come back and not have to worry about things like dusting, cleaning your kitchen or bathrooms or taking out the garbage. i do all of that for you! and you don't even have to worry about providing</p>

<div class="service" style="left:131px">
  <div class="service-icon"><svg width="46" height="46" viewBox="0 0 46 46" fill="none" stroke="#fff" stroke-width="3"><path d="M8 40 L18 10 Q22 4 26 10"/><rect x="24" y="24" width="16" height="14" rx="6"/><circle cx="32" cy="31" r="3"/></svg></div>
  <h3>Vacuum</h3>
  <p>It is a long established fact that a reader<br>will be distracted by the readable</p>
  <a href="#">Learn More -&gt;</a>
</div>
<div class="service" style="left:451px">
  <div class="service-icon"><svg width="46" height="46" viewBox="0 0 46 46" fill="#fff"><path d="M6 40 L14 24 L32 24 L40 40Z"/><path d="M23 6l2 5 5 2-5 2-2 5-2-5-5-2 5-2z"/><path d="M34 8l1 3 3 1-3 1-1 3-1-3-3-1 3-1z"/></svg></div>
  <h3>Wash Floors</h3>
  <p>It is a long established fact that a reader<br>will be distracted by the readable</p>
  <a href="#">Learn More -&gt;</a>
</div>
<div class="service" style="left:769px">
  <div class="service-icon"><svg width="46" height="46" viewBox="0 0 46 46" fill="none" stroke="#fff" stroke-width="3"><rect x="8" y="6" width="30" height="34"/><path d="M8 6 L18 12 L18 36 L8 40 M38 6 L28 12 L28 36 L38 40"/></svg></div>
  <h3>Wash Windows</h3>
  <p>It is a long established fact that a reader<br>will be distracted by the readable content</p>
  <a href="#">Learn More -&gt;</a>
</div>

<!-- green feature -->
<div class="abs feature-bg" role="img" aria-label="Green-tinted photo of a bright living room with houseplants"></div>
<div class="abs feature-card">
  <h2>What makes green cleaning<br>environmentally friendly?</h2>
  <ul>
    <li>We use unscented, non-toxic, chemical-free cleaners</li>
    <li>We use vinegar as an antiseptic and deodorizer when needed, as<br>well as for windows and mirrors</li>
    <li>We use baking soda if we need more aggressive scrubbing</li>
    <li>We use a HEPA-filter vacuum for allergen relief</li>
  </ul>
  <span class="btn">Read more</span>
</div>
<div class="abs feature-photo" role="img" aria-label="Photo of a woman vacuuming a carpet by a bright window"></div>

<!-- news -->
<h2 class="section-title" style="top:1860px">Latest News</h2>

<article class="news" style="left:91px">
  <div class="news-photo" role="img" aria-label="Photo of a mop cleaning a wooden floor" style="background:radial-gradient(ellipse 90px 30px at 170px 150px,rgba(70,130,200,.75),rgba(70,130,200,0)),radial-gradient(ellipse 60px 50px at 270px 130px,rgba(240,200,40,.8),rgba(240,200,40,0)),linear-gradient(170deg,#dcd8d2 0%,#b8a48c 55%,#8c7b68 100%)">
    <div class="date"><div class="d">02<small>JUN</small></div><div class="y">2017</div></div>
  </div>
  <h3>Porro quisquam est</h3>
  <p>&nbsp;It has survived not only five centuries, but also<br>the leap into electronic typesetting,</p>
  <a href="#">Read More »</a>
</article>
<article class="news" style="left:443px">
  <div class="news-photo" role="img" aria-label="Photo of a woman scrubbing a kitchen cabinet" style="background:radial-gradient(ellipse 50px 50px at 30px 40px,rgba(70,140,50,.8),rgba(70,140,50,0)),radial-gradient(ellipse 70px 60px at 210px 80px,rgba(200,160,90,.8),rgba(200,160,90,0)),radial-gradient(ellipse 60px 40px at 230px 150px,rgba(190,50,110,.7),rgba(190,50,110,0)),linear-gradient(170deg,#e6e8e4 0%,#c9d4d6 50%,#6f5a4c 100%)">
    <div class="date"><div class="d">02<small>JUN</small></div><div class="y">2017</div></div>
  </div>
  <h3>Dolorem ipsum quia</h3>
  <p>&nbsp;It has survived not only five centuries, but also the<br>leap into electronic typesetting, remaining</p>
  <a href="#">Read More »</a>
</article>
<article class="news" style="left:797px">
  <div class="news-photo" role="img" aria-label="Photo of a woman wiping a sunny window" style="background:radial-gradient(ellipse 60px 40px at 240px 60px,rgba(240,200,40,.85),rgba(240,200,40,0)),radial-gradient(ellipse 70px 80px at 150px 110px,rgba(60,60,65,.6),rgba(60,60,65,0)),linear-gradient(170deg,#eef4f8 0%,#c9dcea 55%,#9eb6c6 100%)">
    <div class="date"><div class="d">02<small>JUN</small></div><div class="y">2017</div></div>
  </div>
  <h3>Neque porro quisquam</h3>
  <p>&nbsp;It has survived not only five centuries, but also the<br>leap into electronic typesetting, remaining</p>
  <a href="#">Read More »</a>
</article>

<!-- footer -->
<svg class="abs" style="left:0;top:2320px" width="1200" height="70" viewBox="0 0 1200 70">
  <path d="M0 70 Q600 -20 1200 70Z" fill="#1f6b12"/>
  <path d="M0 70 Q600 -6 1200 70Z" fill="#232323"/>
</svg>
<footer class="abs footer"></footer>
<div class="logo-mark" style="left:104px;top:2465px;width:76px;height:76px"></div>
<div class="brand" style="left:195px;top:2489px;color:#fff;font-size:20px">MAPLE SPARKLE</div>

<div class="foot-head" style="left:415px">Contact Us</div>
<div class="foot-text" style="left:415px;top:2471px">Address : P.O. Box 2210<br>Ottawa, ON K1P 5J2<br>Phone : 613-555-0142<br>Email : info@tidyroost.example</div>

<div class="foot-head" style="left:662px">Join our mailing list</div>
<div class="foot-text" style="left:663px;top:2473px;line-height:19px">Your about us information would fit<br>here nicely.</div>
<div class="abs mail-input">Email address</div>
<div class="abs mail-btn">Submit</div>

<div class="foot-head" style="left:949px">Follow us out there</div>
<div class="social" style="left:951px;top:2484px;gap:16px"><span style="background:#fff"></span><span style="background:#fff"></span><span style="background:#fff"></span><span style="background:#fff"></span></div>

<div class="abs foot-rule"></div>
<div class="abs copyright">Copyright © 2017 All Rights Reserved</div>

</body>
</html>
```